Business card design needed

I need a business card for my new Food & Lifestyle Coaching business - "Bloomvale Food & Lifestlye Coaching"

i already have a logo and would like to have that incorporated into the business card, obviously.

i would like a design that says "fresh" and "funky" - my target market is female, aged 20-45 so i want something that will stand out to them when they see it.

My "Company Colour" is Apple Green
Updates

Thankyou to everyone who has submitted a design for my project. At this stage i have quite a large number of designs to chose from and with only a short time until my project closes i am focusing now on chosing from those i have already shortlisted so am unfortunately not considering any new desings.

Thankyou again for your interest in my project.

Target Market(s)

Female, Health Conscious (or looking to improve their health/lifestyle), aged between 20-45

Industry/Entity Type

Business

Contact Information for Business Card

Tamsin Corley
Ph: 0417382946
Email: eatwell@marovex.com

Requirements
Must have
• Must include my existing Logo
Nice to have
• Would be nice to incoirporate and appointment card on the back

```html
<!DOCTYPE html>
<html lang="en">
<head>
<meta charset="utf-8">
<title>Bloomvale – Business Card</title>
<link href="https://fonts.googleapis.com/css2?family=Source+Sans+3:ital,wght@0,400;0,600;0,700;1,400&display=swap" rel="stylesheet">
<style>
  :root {
    --apple-green: #78b53a;
    --apple-green-soft: rgba(120, 181, 58, .18);
    --apple-green-faint: rgba(120, 181, 58, 0);
    --ink: #2a2a2a;
    --card-white: #f7f8f8;
    --card-grey: #e6e8e9;
    --backdrop: #eeeeec;
    --white: #ffffff;
  }
  * { margin: 0; padding: 0; box-sizing: border-box; }
  html, body {
    width: 1200px; height: 880px; overflow: hidden;
    background: var(--backdrop);
    font-family: "Source Sans 3", "Myriad Pro", Arial, sans-serif;
  }
  .canvas { position: relative; width: 1200px; height: 880px; }
  .card {
    position: absolute; left: 260px; width: 680px; height: 390px;
    background: linear-gradient(160deg, var(--card-white) 0%, var(--card-grey) 100%);
    box-shadow: 0 3px 10px rgba(0,0,0,.15);
    overflow: hidden;
  }
  .card--front { top: 40px; }
  .card--back { top: 450px; }
  .card svg.card-art { position: absolute; inset: 0; }

  /* front */
  .brand {
    position: absolute; left: 110px; top: 44px;
  }
  .brand__row { display: flex; align-items: center; gap: 22px; }
  .brand__dot { width: 96px; height: 96px; border-radius: 50%; background: var(--apple-green); flex: none; }
  .brand__name {
    color: var(--ink); font-weight: 600; font-size: 80px; line-height: 1; letter-spacing: 1px;
  }
  .brand__tagline {
    display: block; color: var(--ink); font-weight: 400; font-size: 22px;
    margin-top: 6px; padding-left: 196px;
  }
  .contact-holder {
    position: absolute; left: 52px; top: 282px; width: 220px; color: var(--white);
  }
  .holder-name { font-size: 28px; font-weight: 700; opacity: .92; }
  .holder-role { font-size: 20px; font-style: italic; text-align: right; opacity: .85; margin-top: 2px; }
  .contact-list {
    position: absolute; left: 335px; top: 286px; list-style: none; color: var(--white);
    font-size: 20px; line-height: 36px;
  }
  .contact-list li { display: flex; align-items: center; gap: 12px; }
  .contact-list svg { width: 16px; height: 16px; flex: none; }

  /* back */
  .trail-area {
    position: absolute; left: 24px; top: 0; width: 150px; height: 390px;
    background: linear-gradient(180deg, var(--apple-green-faint) 0%, var(--apple-green-soft) 55%, var(--apple-green-faint) 100%);
    border-radius: 0 0 75px 75px;
  }
  .appointment {
    position: absolute; left: 200px; top: 30px; color: var(--ink);
  }
  .appointment__title { color: var(--apple-green); font-size: 26px; font-weight: 700; }
  .appointment__fields { list-style: none; font-size: 19px; line-height: 30px; margin-top: 6px; }
  .back-brand {
    position: absolute; right: 56px; bottom: 48px; display: flex; align-items: center; gap: 14px;
    color: var(--apple-green); font-weight: 600; font-size: 34px;
  }
  .back-brand__dot { width: 70px; height: 70px; border-radius: 50%; background: var(--apple-green); }
</style>
</head>
<body>
<main class="canvas">

  <section class="card card--front" aria-label="Business card front">
    <svg class="card-art" width="680" height="390" viewBox="0 0 680 390" aria-hidden="true">
      <path d="M0,216 C220,206 460,216 680,238" fill="none" stroke="var(--apple-green)" stroke-width="3"/>
      <path d="M0,232 C220,224 460,236 680,256 L680,390 L0,390 Z" fill="var(--apple-green)"/>
      <line x1="300" y1="282" x2="300" y2="364" stroke="#ffffff" stroke-opacity=".7" stroke-width="2" stroke-dasharray="0 6" stroke-linecap="round"/>
    </svg>

    <h1 class="brand">
      <span class="brand__row">
        <span class="brand__dot" aria-hidden="true"></span>
        <span class="brand__name">Bloomvale</span>
      </span>
      <span class="brand__tagline">Food &amp; Lifestlye Coaching</span>
    </h1>

    <div class="contact-holder">
      <p class="holder-name">Tamsin Corley</p>
      <p class="holder-role">manager</p>
    </div>

    <ul class="contact-list">
      <li>
        <svg viewBox="0 0 16 16" aria-hidden="true"><rect x="4" y="1" width="8" height="14" rx="1.5" fill="none" stroke="#fff" stroke-width="1.6"/><rect x="6" y="3.5" width="4" height="4" fill="#fff"/></svg>
        0417.382.946
      </li>
      <li>
        <svg viewBox="0 0 16 16" aria-hidden="true"><rect x="1" y="3" width="14" height="10" rx="1" fill="#fff"/><path d="M1.5,3.5 L8,9 L14.5,3.5" fill="none" stroke="var(--apple-green)" stroke-width="1.4"/></svg>
        eatwell@marovex.com
      </li>
    </ul>
  </section>

  <section class="card card--back" aria-label="Appointment card back">
    <div class="trail-area" role="img" aria-label="Dotted green vine trail decoration"></div>

    <div class="appointment">
      <h2 class="appointment__title">Your Next Appointment:</h2>
      <ul class="appointment__fields">
        <li>With:</li>
        <li>Date:</li>
        <li>Time:</li>
      </ul>
    </div>

    <div class="back-brand">
      <span class="back-brand__dot" aria-hidden="true"></span>
      <span>Bloomvale</span>
    </div>
  </section>

</main>
</body>
</html>
```